Business Card Design. For a portrait and wedding photography business

Velvet Frame Studios Weddings, Portraits, Bar/Bat Mitzvah, Sweet 16's, On the Cutting Edge of Digital Photography Corporate Events High Quality Photography at an Affordable PricesCustom Wedding Packages.Custom Designed Album, Thank you cardsExpert Photo Editing and Retouching

Target Market(s)

Families for family portraits, head shots for business cards,, wedding clients, Suite 16's, bar/bat mitzvah, parties, and corporate events,
.

Industry/Entity Type

Wedding

Contact Information for Business Card

Daniel T. Ashworth 42 Linden Lane Cornwall, N.Y. 12634 By Appointment Only

Font styles to use
Script
Other font styles liked:
• Time New Romen

Requirements
Must have
• I would like to use one of the photograph I uploaded I would prefer to let the designer choose based on their expertise.
Nice to have
• Leave it up to the designer
Should not have
• The card should not be too dark

```html
<!DOCTYPE html>
<html lang="en">
<head>
<meta charset="utf-8">
<title>Velvet Frame Studios – Business Card</title>
<link rel="stylesheet" href="https://fonts.googleapis.com/css2?family=Arimo:wght@400&display=swap">
<style>
  :root {
    --bg-outer: #2a2c2c;
    --bg-inner: #161818;
    --card-white: #fdfefe;
    --card-shade: #e9ecec;
    --ink: #2b2d2d;
    --ink-soft: #3a3c3c;
    --band-light: #c9cbcb;
    --band-dark: #6d7070;
    --rule: #3a3c3c;
  }
  html, body {
    margin: 0;
    padding: 0;
    overflow: hidden;
    background: var(--bg-outer);
  }
  .business-card {
    display: block;
    width: 702px;
    height: 1200px;
  }
  .holder-name {
    font-family: "Arimo", Arial, sans-serif;
    font-size: 29px;
    fill: var(--ink);
  }
  .holder-address {
    font-family: "Arimo", Arial, sans-serif;
    font-size: 15.5px;
    fill: var(--ink);
  }
  .services-text {
    font-family: "Arimo", Arial, sans-serif;
    font-size: 16.5px;
    fill: var(--ink-soft);
  }
</style>
</head>
<body>
<svg class="business-card" width="702" height="1200" viewBox="0 0 702 1200" xmlns="http://www.w3.org/2000/svg">
  <defs>
    <radialGradient id="glow" cx="50%" cy="42%" r="65%">
      <stop offset="0" stop-color="#4a4d4d"/>
      <stop offset="1" stop-color="#1b1d1d"/>
    </radialGradient>
    <radialGradient id="inner-glow" cx="50%" cy="45%" r="60%">
      <stop offset="0" stop-color="#3c3f3f"/>
      <stop offset="1" stop-color="#121414"/>
    </radialGradient>
    <linearGradient id="band" x1="0" y1="0" x2="0" y2="1">
      <stop offset="0" stop-color="#7b7e7e"/>
      <stop offset="0.45" stop-color="#a9acac"/>
      <stop offset="1" stop-color="#d6d8d8"/>
    </linearGradient>
    <radialGradient id="band-sheen" cx="50%" cy="100%" r="60%">
      <stop offset="0" stop-color="#eef0f0" stop-opacity="0.8"/>
      <stop offset="1" stop-color="#eef0f0" stop-opacity="0"/>
    </radialGradient>
    <linearGradient id="monogram-fill" x1="0" y1="0" x2="1" y2="1">
      <stop offset="0" stop-color="#f3f5f5"/>
      <stop offset="1" stop-color="#dfe3e3"/>
    </linearGradient>
    <filter id="soft-shadow" x="-20%" y="-20%" width="140%" height="140%">
      <feDropShadow dx="0" dy="0" stdDeviation="5" flood-color="#000" flood-opacity="0.45"/>
    </filter>
    <filter id="text-lift">
      <feDropShadow dx="0" dy="1" stdDeviation="0.6" flood-color="#ffffff" flood-opacity="0.6"/>
    </filter>
  </defs>

  <!-- background -->
  <rect class="backdrop" width="702" height="1200" fill="url(#glow)"/>
  <rect class="inner-panel" x="31" y="66" width="640" height="1067" fill="url(#inner-glow)"/>
  <line class="horizon-line" x1="0" y1="948" x2="702" y2="948" stroke="#0d0e0e" stroke-width="2"/>

  <!-- stacked white panels -->
  <g class="panel-stack" filter="url(#soft-shadow)">
    <path class="panel-back-left" d="M149 380 L203 381 L203 898 L149 898 Z" fill="var(--card-shade)"/>
    <path class="panel-back-right" d="M496 588 L521 594 L521 898 L496 898 Z" fill="var(--card-shade)"/>
    <path class="panel-main" d="M203 252 Q370 256 496 310 L496 893 L203 893 Z" fill="var(--card-white)"/>
  </g>

  <!-- contact details -->
  <text class="holder-name" x="345" y="464" text-anchor="middle">Daniel T. Ashworth</text>
  <line class="name-rule" x1="216" y1="480" x2="474" y2="480" stroke="var(--rule)" stroke-width="1.5"/>
  <text class="holder-address" x="355" y="498" text-anchor="middle">42 Linden Lane Cornwall,</text>
  <text class="holder-address" x="355" y="517" text-anchor="middle">N.Y. 12634</text>

  <!-- monogram area -->
  <rect class="monogram" x="215" y="619" width="255" height="205" rx="6" fill="url(#monogram-fill)" role="img" aria-label="Embossed script monogram initial"/>

  <!-- services band -->
  <rect class="services-band" x="31" y="901" width="640" height="232" fill="url(#band)"/>
  <rect class="services-band-sheen" x="31" y="901" width="640" height="232" fill="url(#band-sheen)"/>
  <g class="services-list" text-anchor="middle" filter="url(#text-lift)">
    <text class="services-text" x="352" y="940">Velvet Frame Studios Weddings, Portraits,</text>
    <text class="services-text" x="352" y="961">Bar/Bat Mitzvah, Sweet 16's,</text>
    <text class="services-text" x="352" y="983">On the Cutting Edge of Digital Photography Corporate Events</text>
    <text class="services-text" x="352" y="1004">High Quality Photography at an Affordable Prices</text>
    <text class="services-text" x="352" y="1025">Custom Wedding Packages.</text>
    <text class="services-text" x="352" y="1048">Custom Designed Album, Thank you cards</text>
    <text class="services-text" x="352" y="1069">Expert Photo Editing and Retouching.</text>
  </g>
</svg>
</body>
</html>
```